VARLEN Consulting Services “Coming Soon” Landing Page

MORE INTO IN Design Brief for Web Designer document attached

1. Project Overview
Client: VARLEN Consulting Services
Project: Build a static, responsive “Coming Soon” landing page (HTML/CSS/JS)
Timeline: Target launch date in June 7, 2025
Point of Contact: Martin Hallowby (Managing Director)
 • Email: mart@varlenconsulting.example
 • Phone: 415-738-2094
Background:
VARLEN Consulting Services is a boutique IT consultancy specializing in enterprise cloud solutions, microservices, FlowMesh migrations, and AGENTIC AI-driven integrations. We are launching a new website to capture CIO-level leads, build brand awareness, and communicate our key value propositions before the full site goes live. This “Coming Soon” page should reflect our brand identity, target CIO and enterprise IT leaders, and collect email addresses for early access to whitepapers, case studies, and consultations.

2. Goals & Objectives
1. Brand Reinforcement
• Convey a contemporary, corporate, and professional look that aligns with VARLEN’s positioning as a specialized, agile, high-ROI consultancy.
• Utilize our brand colors (green, red, blue, gold) and typography (Segoe UI) consistently.
2. Lead Generation
• Implement a simple email-capture form (“Notify Me”) that submits to mailto:info@varlenconsulting.example.
• Convey clear messaging so visitors understand why they should sign up (exclusive early insights, whitepapers, invitations to consult).
3. Enterprise Leadership-Focused Messaging
• Immediately communicate our core value proposition (“Enterprise Modernization Reimagined”) and differentiation versus larger consulting firms.
• Introduce AGENTIC AI use cases to demonstrate cutting-edge capabilities.
4. Responsive & Accessible
• Build a mobile-first responsive design using a 12-column grid.
• Follow best practices for HTML5 markup, CSS3, and lightweight JS (for countdown timer).
5. SEO & Technical Must-Haves
• Include basic SEO metadata and Open Graph tags.
• Provide a favicon placeholder.
• Placeholder for a Privacy Policy link in the footer.

Designs look the same

VARLEN Consulting Services is a boutique IT consultancy specializing in enterprise cloud solutions, microservices, FlowMesh migrations, and AGENTIC AI-driven integrations.

• Below are our primary brand colors with hex codes (derived from CMYK values in the uploaded “Color and Font.jpg”): • Green (Globe Icon): #3BFF05 • Red (Q-Shape Icon): #EF1C03 • Blue (Circle Icon): #456EFF • Gold (Connector Icon): #F7C217 • Dark Gray / Text Color: #1A1A1A Use these colors for text highlights, buttons, icons, and accents. The overall page background is white or very light gray (#F9F9F9) to keep the design clean.
• Colors outside the scheme provided

```html
<!DOCTYPE html>
<html lang="en">
<head>
<meta charset="utf-8">
<title>VARLEN Consulting Services — Coming Soon</title>
<link href="https://fonts.googleapis.com/css2?family=Barlow:wght@600;700;800&family=Open+Sans:wght@400;600;700&display=swap" rel="stylesheet">
<style>
:root{
  --green:#3BFF05;
  --green-text:#35d60a;
  --red:#EF1C03;
  --blue:#456EFF;
  --gold:#F7C217;
  --ink:#1A1A1A;
  --muted:#444;
  --light:#F2F2F2;
  --navy:#0b1140;
  --navy-2:#16207a;
  --tag-bg:#ffd4cc;
}
*{box-sizing:border-box;margin:0;padding:0}
html,body{width:1200px;height:4854px;overflow:hidden}
body{font-family:"Open Sans",sans-serif;color:var(--ink);background:#fff;position:relative}
.section{position:absolute;left:0;width:1200px;overflow:hidden}
.abs{position:absolute}
.display{font-family:"Barlow",sans-serif;font-weight:800;text-transform:uppercase;letter-spacing:.2px}
.hl{color:var(--green-text)}
.center{text-align:center;left:0;width:1200px}
.btn{position:absolute;display:flex;align-items:center;justify-content:center;border-radius:22px;font-size:12px;font-weight:700;text-transform:uppercase;letter-spacing:.3px}
.btn-blue{background:var(--blue);color:#fff}
.btn-gold{background:var(--gold);color:var(--ink)}
.btn-white{background:#fff;color:var(--blue)}
.tag{position:absolute;background:var(--tag-bg);color:var(--red);border:1px solid #f7a899;font-size:12px;font-weight:600;padding:4px 10px;text-transform:uppercase}
.ticks{list-style:none}
.ticks li{position:relative;padding-left:18px;font-size:13px;line-height:18px;color:var(--ink)}
.ticks li::before{content:"";position:absolute;left:0;top:4px;width:10px;height:10px;border-radius:50%;background:var(--gold)}
.ticks li::after{content:"";position:absolute;left:3px;top:6px;width:3px;height:5px;border:solid #fff;border-width:0 1.5px 1.5px 0;transform:rotate(45deg)}
.ticks b{color:var(--blue);font-weight:600}

/* hero */
.hero{top:0;height:680px;background:linear-gradient(120deg,#0a0f3a 0%,#111a5c 55%,#1a1565 100%)}
.brand{left:170px;top:30px;display:flex;align-items:center;gap:10px}
.brand-dot{width:36px;height:36px;border-radius:50%;background:var(--blue)}
.brand-name{font-family:"Barlow",sans-serif;font-weight:700;font-size:30px;color:#fff}
.hero-title{left:170px;top:150px;font-size:52px;line-height:53px;color:#fff}
.hero-sub{left:170px;top:313px;width:450px;font-size:15px;line-height:21px;color:var(--gold)}
.hero-text{left:170px;top:398px;width:460px;font-size:12.5px;line-height:19.6px;color:#fff}
.hero-art{left:620px;top:180px;width:580px;height:400px;background:radial-gradient(ellipse at 55% 50%,#c2338f 0%,#5a2fb0 35%,rgba(30,40,140,.2) 70%,transparent 80%)}

/* about */
.about{top:680px;height:814px;background:#fff}
.about-title{top:92px;font-size:36px;line-height:41px}
.about-text{top:183px;left:225px;width:750px;text-align:center;font-size:12.5px;line-height:19px;color:var(--muted)}
.ring{left:377px;top:68px}
.orb{left:499px;top:426px;width:200px;height:200px;border-radius:50%;background:radial-gradient(circle at 45% 40%,#4fb8ff 0%,#1d5fd6 40%,#0b1d6e 85%)}
.point{position:absolute;font-size:12px;line-height:17px;padding:8px 12px 8px 26px;border-radius:4px;color:var(--ink)}
.point::before{content:"";position:absolute;left:10px;top:12px;width:10px;height:10px;border-radius:50%;background:var(--gold)}
.point b{font-weight:700}
.p-yellow{background:#fff6d6}
.p-blue{background:#eaf0ff}
.p-green{background:#eafbe0}
.dot{position:absolute;width:16px;height:16px;border-radius:50%}

/* notify */
.notify{top:1494px;height:358px;background:var(--light)}
.notify-title{top:48px;font-size:36px}
.notify-text{top:100px;font-size:12.5px;color:var(--ink)}
.signup{left:292px;top:141px;width:607px;height:42px;background:#fff;border-radius:21px;display:flex;align-items:center;padding-left:18px;font-size:12px;color:#555;gap:8px}
.signup .btn{right:0;top:0;width:128px;height:42px;border-radius:21px}
.notify-note{top:200px;font-size:12px;color:var(--gold)}
.countdown{top:234px;display:flex;justify-content:center;gap:28px}
.unit{display:flex;flex-direction:column;align-items:center;gap:12px;font-size:12px}
.digits{display:flex;gap:8px}
.digit{width:34px;height:48px;background:#fff;border-radius:4px;box-shadow:0 2px 6px rgba(0,0,0,.15);display:flex;align-items:center;justify-content:center;font-family:"Barlow",sans-serif;font-weight:700;font-size:34px;color:var(--red)}

/* apart */
.apart{top:1852px;height:399px;background-color:#fff;background-image:linear-gradient(#f1f1f1 1px,transparent 1px),linear-gradient(90deg,#f1f1f1 1px,transparent 1px);background-size:26px 26px}
.apart-title{left:220px;top:82px;font-size:36px}
.apart-list{left:220px;top:144px}
.apart-list li{margin-bottom:16px}
.rating{left:659px;top:55px;width:315px;height:199px;background:var(--blue);border-radius:8px;padding:22px 22px;color:#fff}
.rating-brand{display:flex;align-items:center;gap:8px;font-family:"Barlow",sans-serif;font-weight:700;font-size:18px}
.rating-brand span.sq{width:22px;height:22px;background:#fff;opacity:.85}
.rating-score{margin-top:10px;font-size:13px;font-weight:700}
.rating-score i{font-style:normal;color:var(--gold);letter-spacing:1px}
.bar{height:4px;background:rgba(255,255,255,.75);border-radius:2px;margin-top:12px}
.stats{left:659px;top:264px;width:315px;height:79px;border:2px solid #a9baff;border-radius:6px;background:#fff;display:flex;align-items:center;justify-content:space-around}
.stat{font-family:"Barlow",sans-serif;font-weight:600;font-size:34px;color:#555;position:relative}
.stat::after{content:"";position:absolute;left:0;bottom:-10px;width:100%;height:3px;background:#ddd}
.stats .sep{width:2px;height:44px;background:#ccc}

/* services */
.services{top:2251px;height:857px;background:var(--light)}
.services-title{top:42px;font-size:36px}
.svc-track{left:170px;top:108px;display:flex;gap:19px}
.svc{width:200px;height:275px;background:#fff;padding:28px 12px 0;text-align:center}
.svc svg{width:56px;height:56px}
.svc h3{margin-top:14px;color:var(--blue);font-size:13px;line-height:18px;font-weight:700;text-transform:uppercase}
.svc p{margin-top:8px;font-size:12px;line-height:18px;color:var(--muted)}
.slider{position:absolute;height:2px;background:#ddd}
.slider span{display:block;height:2px;width:45%;background:var(--gold)}
.arrows{position:absolute;display:flex;gap:18px;font-size:22px;color:var(--ink)}
.bv-title{left:220px;top:466px;font-size:36px;line-height:41px}
.bv-list{left:220px;top:613px;width:320px}
.bv-list li{margin-bottom:15px}
.bv-photo{left:627px;top:462px;width:315px;height:345px;background:linear-gradient(160deg,#d8b59a 0%,#b88a70 40%,#e9e2dc 100%);border-radius:4px}

/* agentic */
.agentic{top:3108px;height:796px;background:#fff}
.agentic-title{top:92px;font-size:36px;line-height:42px}
.agentic-text{top:186px;left:270px;width:660px;text-align:center;font-size:12.5px;line-height:19px;color:var(--muted)}
.case-track{left:170px;top:246px;display:flex;gap:22px}
.case{width:270px;height:399px;background:#f8f8f8;padding:16px 16px}
.case-art{height:149px;background:radial-gradient(circle at 50% 55%,#4fd6ff 0%,#1e63d6 40%,#0a1f5c 90%)}
.case h3{margin-top:16px;color:var(--blue);font-size:15px;line-height:18px;font-weight:700;text-transform:uppercase;font-family:"Open Sans",sans-serif}
.case p{margin-top:10px;font-size:12px;line-height:19px;color:var(--muted)}
.case .outcome{margin-top:14px;color:var(--red);font-weight:600}

/* compare */
.compare{top:3904px;height:523px;background:var(--light)}
.compare-title{top:46px;font-size:31px;line-height:34px}
.table{left:220px;top:171px;width:754px;border-collapse:collapse;background:#fff;font-size:12px}
.table th{background:var(--red);color:#fff;font-weight:700;text-transform:uppercase;height:38px;font-size:12.5px}
.table th,.table td{border-right:1px solid #e5e5e5;padding:0 22px}
.table th:last-child,.table td:last-child{border-right:0}
.table td{height:41px;color:var(--ink);line-height:16px;border-bottom:1px solid #eee}
.table col.a{width:166px}.table col.b{width:294px}.table col.c{width:294px}

/* schedule */
.schedule{top:4427px;height:339px;background:linear-gradient(180deg,#0a0f3a 0%,#121a62 100%)}
.schedule-title{top:44px;font-size:56px;color:#fff}
.schedule-sub{top:107px;font-size:15px;color:var(--gold)}
.schedule-text{top:143px;left:300px;width:600px;text-align:center;font-size:12.5px;line-height:19px;color:#fff}
.cloud{top:200px;width:210px;height:150px;background:radial-gradient(ellipse at 50% 60%,#47b6ff 0%,#1c57c9 45%,rgba(20,40,130,0) 75%)}

/* footer */
.footer{top:4766px;height:88px;background:#fff;font-size:12px}
.copy{left:170px;top:36px}
.social{top:24px;width:38px;height:38px;border-radius:50%;background:var(--blue);display:flex;align-items:center;justify-content:center}
.links{left:693px;top:36px;display:flex;gap:14px}
</style>
</head>
<body>

<section class="section hero">
  <div class="abs brand"><span class="brand-dot"></span><span class="brand-name">VARLEN</span></div>
  <h1 class="abs display hero-title">Enterprise<br><span class="hl" style="color:var(--green)">Modernization</span><br>Reimagined</h1>
  <p class="abs hero-sub">Retire legacy systems and transition to secure, cloud-native infrastructure designed for scalability, AI integration, and the future-ready performance.</p>
  <p class="abs hero-text">Today’s leaders don’t have time for templated strategies and slow-moving firms. At VARLEN, we deliver tailored solutions that align with your business objectives, accelerate outcomes, and scale as you grow. Our senior experts work directly with your team to deliver fast, measurable impact—no layers, no delays. From modernizing legacy platforms to enabling intelligent automation, we solve the complex integration challenges others overlook so you can focus on leading the future.</p>
  <a class="btn btn-blue" style="left:170px;top:556px;width:234px;height:38px">Schedule a Consultation</a>
  <div class="abs hero-art" role="img" aria-label="Glowing wireframe cloud with an upload and download arrow"></div>
</section>

<section class="section about">
  <span class="tag" style="left:538px;top:55px">About VARLEN</span>
  <h2 class="abs display center about-title">At VARLEN <span class="hl">Consulting Services,</span><br>We don’t do cookie-cutter.</h2>
  <p class="abs about-text">Imaginea partner that doesn’t hand you a recycled playbook—but builds a smarter path forward that’s all about yourgoals. We roll up our sleeves, work alongside your team, and deliver fast, measurable results that move the needle. While others push templates, we unlock possibilities—modern systems, real efficiency, and AI that actually works. No fluff. No junior handoffs. Just bold execution that gets you ahead—and keeps you there</p>
  <svg class="abs ring" width="446" height="446" viewBox="0 0 446 446" aria-hidden="true">
    <circle cx="223" cy="223" r="222" fill="none" stroke="#cfcfcf" stroke-width="1.5" stroke-dasharray="6 6"/>
    <circle cx="223" cy="223" r="178" fill="none" stroke="#e2e2e2" stroke-width="1"/>
  </svg>
  <div class="abs orb" role="img" aria-label="Blue sphere with glowing clouds"></div>
  <div class="point p-yellow" style="left:467px;top:296px;width:264px"><b>Smarter Spend:</b> High impact. Low overhead. We outperform the big firms without their price tags.</div>
  <div class="point p-blue" style="left:220px;top:447px;width:262px"><b>Speed That Scales:</b> Rapid execution means you see value faster—and scale without friction.</div>
  <div class="point p-green" style="left:706px;top:447px;width:268px"><b>Senior Access, Always:</b> Speak directly to the experts. No junior filters. No delays.</div>
  <div class="point p-green" style="left:258px;top:656px;width:266px"><b>Elite Expertise, Zero Fluff:</b> Our DNA is Nimbra, FlowMesh, and bleeding-edge AI.</div>
  <div class="point p-blue" style="left:669px;top:656px;width:267px"><b>Custom Paths to Modernization:</b> Your transformation, built to fit and built to last.</div>
  <span class="dot" style="left:422px;top:354px;background:var(--red)"></span>
  <span class="dot" style="left:780px;top:384px;background:var(--blue)"></span>
  <span class="dot" style="left:363px;top:565px;background:var(--green-text)"></span>
  <span class="dot" style="left:766px;top:540px;background:var(--green-text)"></span>
  <span class="dot" style="left:446px;top:619px;background:var(--blue)"></span>
  <span class="dot" style="left:610px;top:700px;background:var(--red)"></span>
</section>

<section class="section notify">
  <h2 class="abs display center notify-title">Be the first to know when <span class="hl">we go live.</span></h2>
  <p class="abs center notify-text">Join our list to receive early access to whitepapers, case studies, and consultation opportunities.</p>
  <form class="abs signup" action="mailto:info@varlenconsulting.example">
    <svg width="14" height="11" viewBox="0 0 14 11" aria-hidden="true"><rect x="0.5" y="0.5" width="13" height="10" fill="#333"/><path d="M1 1l6 5 6-5" stroke="#fff" fill="none"/></svg>
    <span>Enter your email here</span>
    <span class="btn btn-blue">Notify Me</span>
  </form>
  <p class="abs center notify-note">*We respect your time and inbox. No spam—just strategic insights.</p>
  <div class="abs center countdown">
    <div class="unit"><div class="digits"><span class="digit">3</span><span class="digit">0</span></div>Days</div>
    <div class="unit"><div class="digits"><span class="digit">1</span><span class="digit">2</span></div>Hours</div>
    <div class="unit"><div class="digits"><span class="digit">0</span><span class="digit">7</span></div>Minutes</div>
    <div class="unit"><div class="digits"><span class="digit">1</span><span class="digit">1</span></div>Seconds</div>
  </div>
</section>

<section class="section apart">
  <h2 class="abs display apart-title">What sets <span class="hl">us apart</span></h2>
  <ul class="abs ticks apart-list">
    <li><b>Tailored Execution</b> directly with IT and business strategy</li>
    <li><b>Accelerated ROI</b> land improved TCO metrics</li>
    <li><b>Faster Turnaround Times</b> traditional consulting timelines</li>
    <li><b>Direct Access to Experts</b> no layers of junior consultants</li>
    <li><b>Scalable, Secure Hybrid</b> Cloud Architecturesbuilt to last</li>
    <li><b>Embedded AGENTIC AI</b> for next-gen modernization intelligence</li>
  </ul>
  <div class="abs rating">
    <div class="rating-brand"><span class="sq"></span>ABCD COMPANY</div>
    <div class="rating-score">5.0 Excellent <i>★★★★★</i></div>
    <div class="bar" style="width:100%;margin-top:18px"></div>
    <div class="bar" style="width:100%"></div>
    <div class="bar" style="width:70%;margin-top:26px"></div>
    <div class="bar" style="width:100%"></div>
  </div>
  <div class="abs stats"><span class="stat">100K+</span><span class="sep"></span><span class="stat">100K+</span></div>
</section>

<section class="section services">
  <h2 class="abs display center services-title">Our core <span class="hl">services</span></h2>
  <div class="abs svc-track">
    <article class="svc">
      <svg viewBox="0 0 56 56" aria-hidden="true"><circle cx="28" cy="28" r="9" fill="none" stroke="#111" stroke-width="4"/><g stroke="#111" stroke-width="4"><path d="M28 8v8M28 40v8M8 28h8M40 28h8M14 14l6 6M36 36l6 6M42 14l-6 6M14 42l6-6"/></g><g fill="#111"><circle cx="28" cy="6" r="3"/><circle cx="28" cy="50" r="3"/><circle cx="6" cy="28" r="3"/><circle cx="50" cy="28" r="3"/></g></svg>
      <h3>Microservice<br>Architectures</h3>
      <p>Fault-tolerant, scalable services that integrate with legacy systems—delivered faster than legacy consulting firms.</p>
    </article>
    <article class="svc">
      <svg viewBox="0 0 56 56" aria-hidden="true"><path d="M14 40a10 10 0 0 1 2-20 14 14 0 0 1 26 4 8 8 0 0 1 0 16z" fill="#111"/></svg>
      <h3>Nimbra Integration<br>Architecture</h3>
      <p>Nimbra-native solutions tailored for your enterprise—built for scale, speed, and resilience.</p>
    </article>
    <article class="svc">
      <svg viewBox="0 0 56 56" aria-hidden="true"><path d="M14 36a9 9 0 0 1 2-18 13 13 0 0 1 24 3 8 8 0 0 1 0 15z" fill="#111"/><g fill="#fff"><circle cx="22" cy="27" r="3"/><circle cx="34" cy="27" r="3"/><circle cx="28" cy="22" r="3"/></g><path d="M28 36v10M20 36v8M36 36v8" stroke="#111" stroke-width="3"/></svg>
      <h3>FlowMesh Migration<br>&amp; Optimization</h3>
      <p>Minimized downtime. Maximized value. Precision-driven strategies over templates.</p>
    </article>
    <article class="svc">
      <svg viewBox="0 0 56 56" aria-hidden="true"><path d="M16 22a7 7 0 0 1 2-14 10 10 0 0 1 19 2 6 6 0 0 1 0 12z" fill="#111"/><path d="M28 22v10M10 32h36M10 32v6M28 32v6M46 32v6" stroke="#111" stroke-width="3" fill="none"/><g fill="#111"><rect x="4" y="38" width="12" height="10"/><rect x="22" y="38" width="12" height="10"/><rect x="40" y="38" width="12" height="10"/></g></svg>
      <h3>Hybrid Integration<br>Solutions</h3>
      <p>Cloud/on-premise integrations without the cost of multinational overhead.</p>
    </article>
    <article class="svc">
      <svg viewBox="0 0 56 56" aria-hidden="true"><rect x="12" y="16" width="32" height="28" rx="8" fill="#111"/><circle cx="22" cy="29" r="4" fill="#fff"/><circle cx="34" cy="29" r="4" fill="#fff"/><path d="M28 16V8" stroke="#111" stroke-width="3"/><circle cx="28" cy="7" r="3" fill="#111"/><rect x="6" y="24" width="5" height="12" fill="#111"/><rect x="45" y="24" width="5" height="12" fill="#111"/></svg>
      <h3>Agentic AI<br>Enablement</h3>
      <p>Agents that optimize decisions, monitor workflows, and enrich data across your entire enterprise architecture.</p>
    </article>
  </div>
  <div class="slider" style="left:170px;top:409px;width:860px"><span></span></div>
  <div class="arrows" style="left:962px;top:392px"><span>←</span><span>→</span></div>

  <h2 class="abs display bv-title">Business value<br>for <span class="hl">enterprise</span><br>leadership</h2>
  <ul class="abs ticks bv-list">
    <li><b>Efficiency:</b> Agile methods deliver faster results with less rework</li>
    <li><b>Cost-Effectiveness:</b> Custom-fit solutions tailored to your enterprise</li>
    <li><b>Scalability:</b> Cloud-native, legacy-compatible, and AI-optimized architectures</li>
    <li><b>Security &amp; Compliance:</b> Built-in best practices from day one</li>
  </ul>
  <div class="abs bv-photo" role="img" aria-label="Photo of a smiling businesswoman at a laptop with floating dashboard cards"></div>
</section>

<section class="section agentic">
  <span class="tag" style="left:518px;top:64px">Agentic AI Use Cases</span>
  <h2 class="abs display center agentic-title">Empowering <span class="hl">modernization</span><br>with agentic AI</h2>
  <p class="abs agentic-text">We embed AGENTIC AI into your workflows to deliver context-aware automation, autonomous monitoring, and real-time decisions.</p>
  <div class="abs case-track">
    <article class="case">
      <div class="case-art" role="img" aria-label="Glowing circuit chip illustration"></div>
      <h3>Autonomous Exception Handling</h3>
      <p>Agents monitor, classify, and route integration failures in real time - applying business rules or escalating only when needed.</p>
      <p class="outcome">Outcome: reduced downtime, lower support overhead, and the faster resolution.</p>
    </article>
    <article class="case">
      <div class="case-art" role="img" aria-label="Neon workflow network illustration"></div>
      <h3>Dynamic Workflow Optimization</h3>
      <p>Agents monitor system performance and metadata to restructure or reroute workflows dynamically without redeployment.</p>
      <p class="outcome">Outcome: improved efficiency, fewer failed transactions, and real-time adaptability.</p>
    </article>
    <article class="case">
      <div class="case-art" role="img" aria-label="Data center with glowing shield illustration"></div>
      <h3>Intelligent Data Enrichment</h3>
      <p>AI agents enrich payloads by referencing external sources (APIs, DBs, LLMs), auto-filling missing fields or standardizing formats before delivery.</p>
      <p class="outcome">Outcome: cleaner data, reduced manual cleanup, faster processing.</p>
    </article>
    <article class="case">
      <div class="case-art" role="img" aria-label="Glowing orchestration hub illustration"></div>
      <h3>Context-Aware Orchestration</h3>
      <p>Agents orchestrate API sessions, monitor workflows, choosing paths based on SLAs, and business priorities.</p>
      <p class="outcome">Outcome: smarter routing, lower maintenance burden.</p>
    </article>
  </div>
  <div class="slider" style="left:170px;top:673px;width:860px"><span></span></div>
  <div class="arrows" style="left:962px;top:656px"><span>←</span><span>→</span></div>
  <a class="btn btn-blue" style="left:422px;top:703px;width:173px;height:42px">Schedule a Demo</a>
  <a class="btn btn-gold" style="left:603px;top:703px;width:175px;height:42px">Explore All Cases</a>
</section>

<section class="section compare">
  <h2 class="abs display center compare-title">Smart IT and business leaders are moving<br>fast-<span class="hl">here’s why</span> they’re <span class="hl">choosing agile</span> over<br>traditional consulting</h2>
  <table class="abs table">
    <colgroup><col class="a"><col class="b"><col class="c"></colgroup>
    <thead><tr><th>Aspect</th><th>VARLEN Consulting Services</th><th>Traditional Industry Giants</th></tr></thead>
    <tbody>
      <tr><td>Approach</td><td>Tailored, agile execution</td><td>Standardized, rigid frameworks</td></tr>
      <tr><td>Turnaround Time</td><td>Accelerated</td><td>Average to extended timelines</td></tr>
      <tr><td>Cost Efficiency</td><td>Transparent pricing</td><td>Premium costs &amp; overhead</td></tr>
      <tr><td>Expert Accessibility</td><td>Direct access to specialists</td><td>Layers of account managers</td></tr>
      <tr><td>Scalability Focus</td><td>Hyper-focused on your enterprise needs</td><td>Generic, one-size-fits-all solutions</td></tr>
      <tr><td>Innovation &amp; AI</td><td>Embedded AGENTIC AI &amp; adaptive architectures</td><td>Legacy automation, limited adaptability</td></tr>
    </tbody>
  </table>
</section>

<section class="section schedule">
  <h2 class="abs display center schedule-title">Schedule a <span style="color:var(--green)">consultation</span></h2>
  <p class="abs center schedule-sub">Let’s Reimagine Your Enterprise Together</p>
  <p class="abs schedule-text">Legacy isn’t a roadmap. It’s a roadblock. Let’s architect what’s next—secure, scalable, AI-enabled, and aligned with your business goals.</p>
  <div class="abs cloud" style="left:168px" role="img" aria-label="Glowing blue cloud on a circuit platform"></div>
  <div class="abs cloud" style="left:812px" role="img" aria-label="Glowing blue cloud on a circuit platform"></div>
  <a class="btn btn-gold" style="left:420px;top:208px;width:204px;height:40px">Book a Strategy Session</a>
  <a class="btn btn-white" style="left:637px;top:208px;width:145px;height:40px">Contact Us</a>
</section>

<footer class="section footer">
  <p class="abs copy">© 2025 VARLEN Consulting Services. All rights reserved.</p>
  <a class="abs social" style="left:553px" aria-label="Professional network profile"></a>
  <a class="abs social" style="left:604px" aria-label="Email us" href="mailto:info@varlenconsulting.example">
    <svg width="16" height="12" viewBox="0 0 16 12" aria-hidden="true"><rect x="0.5" y="0.5" width="15" height="11" rx="1" fill="#fff"/><path d="M1 1l7 6 7-6" stroke="var(--blue)" stroke-width="1.4" fill="none"/></svg>
  </a>
  <nav class="abs links"><a>Inmrint</a><a>Privacy Policy</a><a>Cookies</a><a>Terms &amp; Conditions</a></nav>
</footer>

</body>
</html>
```